Torvel, Inc. new buisness cards - brand guide included

We need new business cards. SLEAK SIMPLE FINANCE. They must include a place for NAME, TITLE, CELL, OFFICE PHONE, EMAIL. they also must include our services across the bottom. AIR, OCEAN, FTL, LTL, EXPRESS. for reference this will be being handed to some of the most prestigious shipping companies in a america.

Target Market(s)

Finance and corporate

Contact Information for Business Card

We need new business cards. SLEAK SIMPLE FINANCE. They must include a place for NAME, TITLE, CELL, OFFICE PHONE, EMAIL. they also must include our services across the bottom. AIR, OCEAN, FTL, LTL, EXPRESS.

Requirements
Must have
• We need new business cards. SLEAK SIMPLE FINANCE. They must include a place for NAME, TITLE, CELL, OFFICE PHONE, EMAIL. they also must include our services across the bottom. AIR, OCEAN, FTL, LTL, EXPRESS.
Nice to have
• USE THE COLORS AND LOGO IN THE BRAND GUIDE :)

```html
<!DOCTYPE html>
<html lang="en">
<head>
<meta charset="utf-8">
<title>Torvel, Inc. — Business Cards</title>
<link rel="stylesheet" href="https://fonts.googleapis.com/css2?family=Montserrat:wght@300;400;600;700&family=Source+Sans+3:wght@400;600&display=swap">
<style>
  :root {
    --backdrop: #262626;
    --card-dark: #464646;
    --card-dark-edge: #3c3c3c;
    --card-light: #f3f3f3;
    --gold: #c9bb9b;
    --ink: #2b2b2b;
    --ink-soft: #3a3a3a;
  }
  * { margin: 0; padding: 0; box-sizing: border-box; }
  html, body {
    width: 1200px; height: 900px; overflow: hidden;
    background: var(--backdrop);
    font-family: "Montserrat", sans-serif;
  }
  .canvas { position: relative; width: 1200px; height: 900px; }

  .card {
    position: absolute; left: 393px; width: 414px; height: 236px;
    overflow: hidden;
  }

  /* Front */
  .card--front {
    top: 190px;
    background: radial-gradient(ellipse at 50% 15%, #4c4c4c 0%, var(--card-dark) 45%, var(--card-dark-edge) 100%);
  }
  .brand {
    position: absolute; display: flex; align-items: center; gap: 10px;
    color: var(--gold); font-family: "Montserrat", sans-serif; font-weight: 400;
  }
  .brand__square { width: 10px; height: 10px; background: var(--gold); flex: none; }
  .card--front .brand {
    left: 0; right: 0; top: 98px; justify-content: center;
    font-size: 34px; letter-spacing: 2px; line-height: 40px;
  }
  .card--front .brand__square { width: 14px; height: 14px; }
  .services {
    position: absolute; left: 0; right: 0; top: 197px; text-align: center;
    color: var(--gold); font-weight: 600; font-size: 9.5px; letter-spacing: 5.2px;
  }
  .band { position: absolute; left: 0; right: 0; height: 11px; background: var(--gold); }
  .card--front .band { bottom: 0; }

  /* Back */
  .card--back {
    top: 474px;
    background: linear-gradient(180deg, #f5f5f5 0%, var(--card-light) 60%, #eeeeee 100%);
    color: var(--ink);
  }
  .card--back .band { top: 0; height: 12px; }
  .tagline-rule { position: absolute; left: 0; top: 37px; width: 29px; height: 1px; background: var(--gold); }
  .tagline {
    position: absolute; left: 35px; top: 33px;
    font-weight: 700; font-size: 9.5px; letter-spacing: 1.3px; line-height: 12px;
    color: var(--ink);
  }
  .card--back .brand {
    right: 36px; top: 46px; font-size: 22px; letter-spacing: 1px; line-height: 26px;
  }
  .holder { position: absolute; left: 35px; top: 93px; }
  .holder__name { font-weight: 600; font-size: 16px; line-height: 20px; color: var(--ink); }
  .holder__title { font-weight: 300; font-size: 13px; line-height: 18px; color: var(--ink-soft); }

  .contact {
    position: absolute; top: 163px;
    font-family: "Source Sans 3", sans-serif; font-size: 8.6px; line-height: 12.3px;
    color: var(--ink-soft); white-space: nowrap;
  }
  .contact--company { left: 35px; }
  .contact--company strong { font-weight: 600; color: var(--ink); }
  .contact--phones { left: 218px; }
  .contact--web { left: 299px; }
</style>
</head>
<body>
<main class="canvas">
  <section class="card card--front" aria-label="Business card front">
    <div class="brand"><span class="brand__square"></span><span class="brand__name">Torvel</span></div>
    <p class="services">AIR. OCEAN. FTL. LTL. EXPRESS.</p>
    <div class="band"></div>
  </section>

  <section class="card card--back" aria-label="Business card back">
    <div class="band"></div>
    <div class="tagline-rule"></div>
    <p class="tagline">BEYOND<br>TRANSPORTATION</p>
    <div class="brand"><span class="brand__square"></span><span class="brand__name">Torvel</span></div>
    <div class="holder">
      <p class="holder__name">Your Name</p>
      <p class="holder__title">position</p>
    </div>
    <p class="contact contact--company"><strong>Torvel, Inc.</strong><br>2210 Harbor Ridge Rd Ste 110<br>Lakeview, WA 98100</p>
    <p class="contact contact--phones">T. 555 014 2290<br>F. 555 014 2290</p>
    <p class="contact contact--web">hello@torvelinc.com<br>www.torvelinc.com</p>
  </section>
</main>
</body>
</html>
```